Kestrel Ark AI Power Point Pitch Deck Design

We are in need of building out a designed version of the attached Power Point. We are a SaaS company focused on utilizing AI to perform marketing functions for small to medium sized businesses. We are looking for a modern SaaS design for this pitch deck.

I have included a mock up of a design for our logo we are thinking of using, we may change the colors but let's go forward with this scheme as shown. We are looking for a matured design here so on places where we use statistics ways to make the statistics pop graphically. Interesting ways to display the information from slide to slide so it doesn't feel repetitive.

Generally speaking this should feel polished enough for us to go to VC firms to raise money. Happy to answer additional questions.

Target Market(s)

VC's

Industry/Entity Type

SaaS

Font styles to use
Sans Serif

Requirements
Must have
• A complete design that feels branded to an AI SaaS
Nice to have
• I'd like graphics within the deck that highlight various statistics
Should not have
• Should not feel cartoon like. It should be professional and modern

```html
<!DOCTYPE html>
<html lang="en">
<head>
<meta charset="utf-8">
<title>Kestrel Ark AI — The Team</title>
<link rel="stylesheet" href="https://fonts.googleapis.com/css2?family=Lato:wght@300;400;700&family=Source+Sans+3:wght@400&display=swap">
<style>
  :root {
    --canvas-white: #ffffff;
    --panel-grey: #f0f0f0;
    --ink: #231f20;
    --blue-mid: #2f6185;
    --blue-light: #3a7aa0;
    --blue-deep: #2c5a7c;
    --blue-darkest: #244a66;
  }
  html, body {
    margin: 0;
    padding: 0;
    width: 1200px;
    height: 675px;
    overflow: hidden;
    background: var(--canvas-white);
  }
  .slide {
    position: relative;
    width: 1200px;
    height: 675px;
    overflow: hidden;
    background: var(--canvas-white);
  }
  .backdrop {
    position: absolute;
    inset: 0;
    width: 1200px;
    height: 675px;
  }
  .slide-title {
    position: absolute;
    left: 696px;
    top: 31px;
    width: 300px;
    margin: 0;
    text-align: center;
    color: var(--canvas-white);
    font-family: "Lato", sans-serif;
    font-weight: 700;
    font-size: 52px;
    line-height: 56px;
    letter-spacing: 0.5px;
  }
  .member {
    position: absolute;
    margin: 0;
    color: var(--ink);
  }
  .member-name {
    position: absolute;
    margin: 0;
    white-space: nowrap;
    font-family: "Lato", sans-serif;
    font-weight: 700;
    font-size: 27px;
    line-height: 1;
  }
  .member-role {
    position: absolute;
    margin: 0;
    white-space: nowrap;
    font-family: "Lato", sans-serif;
    font-weight: 400;
    font-size: 22px;
    line-height: 1;
  }
  .member-role--large { font-size: 26px; }
  .member-bio {
    position: absolute;
    margin: 0;
    width: 580px;
    white-space: nowrap;
    font-family: "Source Sans 3", sans-serif;
    font-weight: 400;
    font-size: 17.2px;
    line-height: 21px;
    color: #2a2a2a;
  }
</style>
</head>
<body>
<main class="slide">
  <svg class="backdrop" viewBox="0 0 2560 1440" preserveAspectRatio="none" aria-hidden="true">
    <polygon class="panel" fill="var(--panel-grey)" points="0,0 1080,0 2520,1440 795,1440 0,645"/>
    <polygon fill="var(--blue-mid)" points="1172,0 2438,0 1805,632"/>
    <polygon fill="var(--canvas-white)" points="1192,0 2418,0 1805,612"/>
    <polygon fill="var(--blue-mid)" points="1212,0 2398,0 1805,592"/>
    <polygon fill="var(--blue-light)" points="2520,0 2560,0 2560,1350 1865,655"/>
    <polygon fill="var(--blue-mid)" points="2560,85 1985,655 2560,1230"/>
    <polygon fill="var(--blue-deep)" points="2560,205 2105,655 2560,1105"/>
    <polygon fill="var(--blue-darkest)" points="2560,325 2225,655 2560,985"/>
  </svg>

  <h1 class="slide-title">THE<br>TEAM</h1>

  <section class="member member--ceo">
    <h2 class="member-name" style="left:98px; top:78px;">DORIAN WHITCOMBE</h2>
    <p class="member-role" style="left:98px; top:120px;">CEO</p>
    <p class="member-bio" style="left:97px; top:151px;">Lorem ipsum dolor sit amet, consectetur adipiscing elit, sed do eiusmod<br>tempor incididunt ut labore et dolore magna aliqua. Quis ipsum suspendisse<br>ultrices gravida. Risus commodo viverra maecenas accumsan lacus vel facili-<br>sis.</p>
  </section>

  <section class="member member--cto">
    <h2 class="member-name" style="left:273px; top:272px;">MATEO LINDQVIST</h2>
    <p class="member-role" style="left:273px; top:311px;">CTO</p>
    <p class="member-bio" style="left:278px; top:354px;">Lorem ipsum dolor sit amet, consectetur adipiscing elit, sed do eiusmod<br>tempor incididunt ut labore et dolore magna aliqua. Quis ipsum suspendisse<br>ultrices gravida. Risus commodo viverra maecenas accumsan lacus vel facili-<br>sis.</p>
  </section>

  <section class="member member--coo">
    <h2 class="member-name" style="left:446px; top:456px;">RAFE OKONJO</h2>
    <p class="member-role member-role--large" style="left:444px; top:493px;">COO/CFO</p>
    <p class="member-bio" style="left:444px; top:533px;">Lorem ipsum dolor sit amet, consectetur adipiscing elit, sed do eiusmod<br>tempor incididunt ut labore et dolore magna aliqua. Quis ipsum suspendisse<br>ultrices gravida. Risus commodo viverra maecenas accumsan lacus vel facili-<br>sis.</p>
  </section>
</main>
</body>
</html>
```